Copper Lantern Podcast Business Card Design

Needing a business card with the logo design provided for Copper Lantern Podcast. I am looking for a modern style that fits the current logo.

Info:
Name: Bao Khanh
Title: Creator/Host
Email: bao@copperlanternpod.com
Phone: (405) 637-2918
www.copperlanternpod.com
Twitter: @coplanternpod
Instagram: @copperlanternpodcast
Facebook: Copper Lantern Podcast

Industry/Entity Type

Business

Font styles to use
Sans Serif

Colors
000000
ffffff

Requirements
Must have
• modern, clean design
Nice to have
• social media contact info

```html
<!DOCTYPE html>
<html lang="en">
<head>
<meta charset="utf-8">
<title>Copper Lantern Podcast – Business Card</title>
<link rel="stylesheet" href="https://fonts.googleapis.com/css2?family=Oswald:wght@500&family=Lato:wght@400;700&display=swap">
<style>
  :root {
    --stage: #e9e7e4;
    --card-white: #ffffff;
    --card-dark: #232323;
    --band: #2b2b2b;
    --ink: #1c1c1c;
    --ink-soft: #555555;
    --on-dark: #ffffff;
    --on-band: #e6e6e6;
  }
  * { box-sizing: border-box; margin: 0; padding: 0; }
  html, body { width: 1200px; height: 1000px; overflow: hidden; }
  body { background: var(--stage); position: relative; font-family: "Lato", sans-serif; }

  .card {
    position: absolute;
    left: 240px;
    width: 697px;
    height: 398px;
    border-radius: 22px;
    overflow: hidden;
  }
  .card--front { top: 82px; background: var(--card-white); }
  .card--back { top: 520px; background: var(--card-dark); }

  /* Front: identity block */
  .identity {
    position: absolute;
    right: 418px;
    top: 170px;
    text-align: right;
  }
  .identity__name {
    font-family: "Oswald", sans-serif;
    font-weight: 500;
    font-size: 36px;
    line-height: 40px;
    letter-spacing: 1.5px;
    color: var(--ink);
  }
  .identity__title {
    font-size: 17px;
    line-height: 22px;
    color: var(--ink);
  }
  .divider {
    position: absolute;
    left: 307px;
    top: 171px;
    width: 2px;
    height: 57px;
    background: var(--ink);
  }
  .contact {
    position: absolute;
    left: 334px;
    top: 168px;
    list-style: none;
  }
  .contact__item {
    display: flex;
    align-items: center;
    height: 21px;
    font-size: 16px;
    color: var(--ink-soft);
  }
  .contact__icon { width: 14px; height: 14px; margin-right: 17px; fill: var(--ink); }

  /* Front: social row */
  .social {
    position: absolute;
    left: 0;
    bottom: 0;
    width: 100%;
    display: flex;
    gap: 4px;
  }
  .social__cell { flex: 1; display: flex; flex-direction: column; align-items: center; }
  .social__mark {
    width: 36px;
    height: 36px;
    border-radius: 5px;
    background: var(--ink);
    margin-bottom: 12px;
  }
  .social__handle {
    width: 100%;
    height: 28px;
    background: var(--band);
    color: var(--on-band);
    font-size: 15px;
    line-height: 28px;
    text-align: center;
  }

  /* Back: brand block */
  .brand {
    position: absolute;
    inset: 0;
    display: flex;
    flex-direction: column;
    align-items: center;
    padding-top: 100px;
    color: var(--on-dark);
    font-weight: 700;
  }
  .brand__square { width: 96px; height: 96px; background: var(--on-dark); margin-bottom: 46px; }
  .brand__name { font-size: 40px; line-height: 44px; letter-spacing: -0.5px; }
  .brand__sub { font-size: 16px; line-height: 22px; letter-spacing: 9px; margin-top: 2px; padding-left: 9px; }
</style>
</head>
<body>

  <section class="card card--front" aria-label="Card front">
    <div class="identity">
      <p class="identity__name">BAO KHANH</p>
      <p class="identity__title">Creator/Host</p>
    </div>
    <div class="divider"></div>
    <ul class="contact">
      <li class="contact__item">
        <svg class="contact__icon" viewBox="0 0 24 24" aria-hidden="true"><path d="M6.6 10.8a15.2 15.2 0 0 0 6.6 6.6l2.2-2.2c.3-.3.7-.4 1-.2 1.1.4 2.3.6 3.6.6.6 0 1 .4 1 1V20c0 .6-.4 1-1 1A17 17 0 0 1 3 4c0-.6.4-1 1-1h3.5c.6 0 1 .4 1 1 0 1.3.2 2.5.6 3.6.1.3 0 .7-.2 1z"/></svg>
        (405) 637-2918
      </li>
      <li class="contact__item">
        <svg class="contact__icon" viewBox="0 0 24 24" aria-hidden="true"><path d="M2 5h20v14H2z M2 5l10 8 10-8" fill="none" stroke="#1c1c1c" stroke-width="0"/><path d="M2 5h20L12 12.5z"/><path d="M2 7.2l10 7.3 10-7.3V19H2z"/></svg>
        bao@copperlanternpod.com
      </li>
      <li class="contact__item">
        <svg class="contact__icon" viewBox="0 0 24 24" aria-hidden="true"><circle cx="12" cy="12" r="10"/><path d="M7 7c2 0 3 1 2.5 2.5S11 12 9.5 13 8 16 9 18c-2-1-4-3-4-6 0-2 1-4 2-5zm8-2c1 1 1 3 3 3 1 1 1 3 0 5-1 1-3 0-3 2s-1 3-2 3c0-2-1-3-2-4s1-3 2-3 1-2 0-3 1-3 2-3z" fill="#ffffff"/></svg>
        www.copperlanternpod.com
      </li>
    </ul>

    <div class="social">
      <div class="social__cell">
        <span class="social__mark" aria-hidden="true"></span>
        <p class="social__handle">Copper Lantern Podcast</p>
      </div>
      <div class="social__cell">
        <span class="social__mark" aria-hidden="true"></span>
        <p class="social__handle">@coplanternpod</p>
      </div>
      <div class="social__cell">
        <span class="social__mark" aria-hidden="true"></span>
        <p class="social__handle">@copperlanternpodcast</p>
      </div>
    </div>
  </section>

  <section class="card card--back" aria-label="Card back">
    <div class="brand">
      <span class="brand__square" aria-hidden="true"></span>
      <p class="brand__name">COPPER LANTERN</p>
      <p class="brand__sub">PODCAST</p>
    </div>
  </section>

</body>
</html>
```